Request for Business Card Design

Hi. My name is Marlena, I am looking for a new business card design for my company, Quillbrook Sensing Systems, LLC. I really like the design you did for Tavel Harvest and was hoping you could do something similar using our full logo and our mark. I am also open to any raised texture design using our mark. I have attached our full logo, which would need to be somewhere on the card, as well as the mark in both outline and full form, as well as our brand colors / guide. The card does not have to be white, as long as our logo and mark appear. I actually like darker colored business cards more, but am open to all options. If you are interested in working with me, please let me know. We would also take the business card design into letterhead design if you can do that.

```html
<!DOCTYPE html>
<html lang="en">
<head>
<meta charset="utf-8">
<title>Quillbrook Sensing Systems – Business Card</title>
<link href="https://fonts.googleapis.com/css2?family=Roboto:wght@400;500;700&display=swap" rel="stylesheet">
<style>
  :root {
    --backdrop: #ababab;
    --paper: #ffffff;
    --charcoal: #404042;
    --ink: #1f1f20;
    --brand-blue: #0a9bc2;
    --rule: #b8b8b8;
  }
  * { box-sizing: border-box; margin: 0; padding: 0; }
  html, body {
    width: 1093px; height: 1200px; overflow: hidden;
    background: var(--backdrop);
    font-family: "Roboto", Arial, sans-serif;
  }
  .card {
    position: absolute; left: 265px;
    width: 576px; height: 356px;
    border-radius: 27px; overflow: hidden;
  }
  .card--front { top: 226px; background: var(--paper); }
  .card--back { top: 621px; background: var(--charcoal); }

  .brand { position: absolute; display: flex; align-items: center; gap: 12px; }
  .brand__dot { width: 44px; height: 44px; border-radius: 50%; background: var(--brand-blue); flex: none; }
  .brand__name {
    font-weight: 700; font-size: 25px; letter-spacing: 2.5px; line-height: 1;
    color: var(--charcoal); text-transform: uppercase;
  }
  .brand__name small {
    display: block; font-size: 11px; font-weight: 700; letter-spacing: 0.6px; margin-top: 5px;
  }
  .card--front .brand { left: 32px; top: 157px; }

  .divider {
    position: absolute; left: 292px; top: 74px; width: 1px; height: 209px;
    background: linear-gradient(to bottom, transparent, var(--rule) 15%, var(--rule) 85%, transparent);
  }
  .contact { position: absolute; left: 312px; top: 90px; color: var(--ink); }
  .contact__name { font-size: 24px; font-weight: 500; color: var(--charcoal); line-height: 1; }
  .contact__title { font-size: 17px; color: var(--brand-blue); line-height: 1.2; margin-top: 2px; }
  .contact__list { list-style: none; margin-top: 14px; }
  .contact__list li { display: flex; align-items: center; gap: 6px; font-size: 17px; line-height: 21px; }
  .contact__list svg { width: 16px; height: 16px; fill: var(--brand-blue); flex: none; }
  .accent { color: var(--brand-blue); }
  .contact__address { font-size: 17px; line-height: 21px; margin-top: 13px; }

  .back__disc {
    position: absolute; left: 270px; top: 20px; width: 310px; height: 310px;
    border-radius: 50%; background: var(--brand-blue);
  }
  .card--back .brand { left: 42px; top: 270px; }
  .card--back .brand__name { color: var(--paper); font-size: 30px; }
  .card--back .brand__name small { font-size: 12px; }
</style>
</head>
<body>
  <section class="card card--front">
    <div class="brand">
      <span class="brand__dot"></span>
      <div class="brand__name">Quillbrook<small>Sensing Systems</small></div>
    </div>
    <div class="divider"></div>
    <div class="contact">
      <h1 class="contact__name">OWEN HARTLEY</h1>
      <p class="contact__title">Managing Director</p>
      <ul class="contact__list">
        <li><svg viewBox="0 0 24 24"><path d="M6.6 10.8a15.2 15.2 0 0 0 6.6 6.6l2.2-2.2a1 1 0 0 1 1-.25 11.4 11.4 0 0 0 3.6.57 1 1 0 0 1 1 1V20a1 1 0 0 1-1 1A17 17 0 0 1 3 4a1 1 0 0 1 1-1h3.5a1 1 0 0 1 1 1c0 1.25.2 2.45.57 3.57a1 1 0 0 1-.25 1z"/></svg>044-210 375 618</li>
        <li><svg viewBox="0 0 24 24"><path d="M2 5h20v14H2zm2 2v.5l8 5 8-5V7l-8 5z"/></svg>info@quillbrook.com</li>
        <li><svg viewBox="0 0 24 24"><path d="M12 2a10 10 0 1 0 0 20 10 10 0 0 0 0-20zm6.9 6h-3a15 15 0 0 0-1.4-3.9A8 8 0 0 1 18.9 8zM12 4c.8 1.2 1.5 2.5 1.9 4h-3.8c.4-1.5 1.1-2.8 1.9-4zM4.3 14a8 8 0 0 1 0-4h3.4a16 16 0 0 0 0 4zm.8 2h3a15 15 0 0 0 1.4 3.9A8 8 0 0 1 5.1 16zm3-8h-3a8 8 0 0 1 4.4-3.9A15 15 0 0 0 8.1 8zM12 20c-.8-1.2-1.5-2.5-1.9-4h3.8c-.4 1.5-1.1 2.8-1.9 4zm2.3-6H9.7a14 14 0 0 1 0-4h4.6a14 14 0 0 1 0 4zm.2 5.9a15 15 0 0 0 1.4-3.9h3a8 8 0 0 1-4.4 3.9zm1.8-5.9a16 16 0 0 0 0-4h3.4a8 8 0 0 1 0 4z"/></svg>www.<span class="accent">quillbrooksensing</span>.com</li>
      </ul>
      <p class="contact__address">421, Address line goes here<br>45452,Country Name</p>
    </div>
  </section>

  <section class="card card--back">
    <div class="back__disc"></div>
    <div class="brand">
      <div class="brand__name">Quillbrook<small>Sensing Systems</small></div>
    </div>
  </section>
</body>
</html>
```